verdant terraces simple classy business card design

my name is owen harlow and I run a gardening business aimed at high class verdant terraces. the business name is verdant terraces and our logo was designed on pixel forum .My clientel are anything from residential homes to businesses. I take pride in my work and know that I offer a service like no other in my area.
The business card will be used to represent my business and I want it to be not only rememberable, but simplistic and modern. Eye catching too. Of course I would like it relatable to gardening and appealing to the correct clientel - those being garden enthusiasts, prestigious homes and businesses that are after top of the line gardening services like no other on the market.
I am not a typical lawn mowing business so I don't want a typical card design that represents that. The gardens I work with are generally million dollar properties with owners who are very garden proud looking for upkeep and guidance from me along with sometimes whole new garden designs. I want the business cards to show to my clients that I take pride, as they do, in their garden. And I want them to know from my card that I am a professional, qualified horticulturist offering them a top of the line service for life. I want them to refer my business on. I want them to look at my business card and see class and professionalism in a modern unique bold way.
The card should be simple with the possibility of the logo on the front being embossed/debossed and my details on the back the card should have a organic garden feel it's very important to me that it is absolutely perfect
I am also very open to ideas and suggestions so look forward to seeing the designs. the business logo has been supplied with this project and I want the card to be double sided

Contact info is
Owen Harlow - Managing Director / Horticulturist
Phone : 0481 526 704
Email: owenharlow@verdantterraces.com.au

Target Market(s)

high class gardens residential and commercial

Industry/Entity Type

Gardener

Contact Information for Business Card

Contact info is
Phone : 0481 526 704

PLEASE MAKE CARD DOUBLE SIDED

Requirements
Must have
• organic simple classy modern feel
• must flow with the current logo that has been supplied with this project
• Double sided
• Must explain in a simple way that I deal with high end gardens and I'm a qualified horticulturist
Nice to have
• embossed debossed logo
Should not have
• shouldn't be to busy or cheap looking

```html
<!DOCTYPE html>
<html lang="en">
<head>
<meta charset="utf-8">
<title>Verdant Terraces — Business Card</title>
<link rel="stylesheet" href="https://fonts.googleapis.com/css2?family=Cormorant+Garamond:wght@500&display=swap">
<style>
  :root {
    --backdrop: #e8e8e6;
    --card: #ffffff;
    --leaf-green: #4f9a3f;
    --ink: #3d3d3d;
    --serif: "Cormorant Garamond", Georgia, serif;
  }
  * { margin: 0; padding: 0; box-sizing: border-box; }
  html, body {
    width: 1054px;
    height: 1200px;
    overflow: hidden;
    background: var(--backdrop);
    font-family: var(--serif);
  }
  .card-set {
    position: relative;
    width: 1054px;
    height: 1200px;
  }
  .card {
    position: absolute;
    top: 230px;
    width: 440px;
    height: 740px;
    background: var(--card);
    box-shadow: 0 6px 18px rgba(0, 0, 0, 0.12);
  }
  .card--front { left: 55px; }
  .card--back { left: 559px; }

  /* Brand lockup */
  .brand {
    position: absolute;
    display: flex;
    align-items: center;
    gap: 18px;
  }
  .brand__dot {
    width: 64px;
    height: 64px;
    border-radius: 50%;
    background: var(--leaf-green);
    flex: none;
  }
  .brand__name {
    font-weight: 500;
    font-size: 30px;
    line-height: 1.25;
    letter-spacing: 0.22em;
    text-transform: uppercase;
    color: var(--leaf-green);
  }
  .card--front .brand { top: 190px; left: 70px; }
  .card--back .brand {
    top: 420px;
    right: 50px;
    flex-direction: column;
    align-items: flex-end;
    gap: 16px;
  }
  .card--back .brand__dot { width: 120px; height: 120px; }
  .card--back .brand__name { font-size: 22px; text-align: right; }

  /* Contact details */
  .contact {
    position: absolute;
    left: 70px;
    right: 0;
    top: 470px;
    color: var(--ink);
  }
  .contact__name-row {
    display: flex;
    align-items: flex-end;
    gap: 10px;
  }
  .contact__name {
    font-weight: 500;
    font-size: 34px;
    font-variant: small-caps;
    letter-spacing: 0.04em;
    line-height: 1;
    white-space: nowrap;
  }
  .contact__rule {
    flex: 1;
    height: 1px;
    background: var(--leaf-green);
    margin-bottom: 4px;
  }
  .contact__role {
    font-weight: 500;
    font-size: 19px;
    margin-top: 8px;
  }
  .contact__lines {
    margin-top: 34px;
    font-weight: 500;
    font-size: 19px;
    line-height: 1.35;
  }
  .contact__email-domain { color: var(--leaf-green); }
</style>
</head>
<body>
  <main class="card-set">
    <section class="card card--front" aria-label="Card front with contact details">
      <div class="brand">
        <span class="brand__dot" aria-hidden="true"></span>
        <span class="brand__name">Verdant Terraces</span>
      </div>
      <div class="contact">
        <div class="contact__name-row">
          <h1 class="contact__name">Owen Harlow</h1>
          <span class="contact__rule"></span>
        </div>
        <p class="contact__role">Managing Director</p>
        <p class="contact__lines">
          0481526704<br>
          owenharlow@<span class="contact__email-domain">verdantterraces.com.au</span>
        </p>
      </div>
    </section>

    <section class="card card--back" aria-label="Card back with brand mark">
      <div class="brand">
        <span class="brand__dot" aria-hidden="true"></span>
        <span class="brand__name">Verdant Terraces</span>
      </div>
    </section>
  </main>
</body>
</html>
```